Netvale - Seafood industry professional promoting page

Hi. I´m in the seafood business with a one man company sourcing and exporting frozen seafood. I need to make a one page homepage for Netvale (from Iceland). The feeling of it should be; Trustworthy, experience and knowledge.
Using as background a picture (or part of it), or a moving video:

http://www1.bryla.is/vefur/myndir/lysingur.jpg
https://clipvault.example/583027416

Main text to be:

- We can help source, market and add value to your seafood business
- Years of experience in seafood trade and production
- Extensive knowledge of fishing, seasonality, production and accreditations

Contact:
torvi@netvale.is
Tel: +3654172093
(with a photo)

p.s. please also make logo look better.

Target Market(s)

Seafood industry

Industry/Entity Type

Business

Logo Text

Netvale

Coding

Coded - Design and coding required

Number of Pages Required

1 page

Colors
0792cd
33a6d7

```html
<!DOCTYPE html>
<html lang="en">
<head>
<meta charset="utf-8">
<title>Netvale – Seafood Sourcing &amp; Export</title>
<link href="https://fonts.googleapis.com/css2?family=Roboto:wght@300;400;500&display=swap" rel="stylesheet">
<style>
  :root {
    --brand-blue: #0792cd;
    --brand-light: #33a6d7;
    --white: #ffffff;
    --nav-bg: rgba(10, 40, 52, 0.82);
    --dark: #14232b;
    --dark-deep: #0c161c;
  }
  * { margin: 0; padding: 0; box-sizing: border-box; }
  html, body { width: 1104px; height: 1200px; overflow: hidden; }
  body { font-family: 'Roboto', Arial, sans-serif; color: var(--white); background: var(--dark); position: relative; }

  .site-header {
    position: absolute; top: 0; left: 0; width: 1104px; height: 57px;
    background: linear-gradient(90deg, rgba(8,34,44,0.92), rgba(12,70,92,0.85));
    z-index: 5;
  }
  .brand { position: absolute; left: 65px; top: 12px; display: flex; align-items: flex-end; gap: 5px; }
  .brand-dot { width: 10px; height: 10px; border-radius: 50%; background: var(--white); margin-bottom: 14px; }
  .brand-name { font-size: 19px; font-weight: 500; color: var(--white); line-height: 1; padding-top: 14px; }
  .main-nav { position: absolute; top: 0; height: 57px; left: 0; width: 100%; }
  .main-nav a { position: absolute; top: 20px; font-size: 14.5px; font-weight: 500; color: var(--white); text-decoration: none; }

  .hero {
    position: absolute; top: 0; left: 0; width: 1104px; height: 524px;
    background:
      radial-gradient(ellipse 420px 160px at 560px 150px, rgba(20,70,80,0.55), transparent 70%),
      radial-gradient(ellipse 500px 140px at 500px 440px, rgba(30,90,90,0.5), transparent 70%),
      linear-gradient(180deg, #1fb3d8 0%, #1893b6 45%, #1a7f93 100%);
  }
  .hero-title { position: absolute; left: 262px; top: 208px; font-size: 97px; font-weight: 400; line-height: 1; letter-spacing: -1px; }
  .hero-sub { position: absolute; left: 269px; top: 306px; font-size: 29px; font-weight: 500; }
  .scroll-cue {
    position: absolute; left: 522px; top: 489px; width: 62px; height: 62px; border-radius: 50%;
    background: var(--brand-blue); z-index: 2;
  }
  .scroll-cue svg { position: absolute; left: 19px; top: 14px; }

  .about { position: absolute; top: 524px; left: 0; width: 1104px; height: 338px; background: var(--brand-blue); }
  .about-photo {
    position: absolute; left: 67px; top: 27px; width: 435px; height: 276px; border: 8px solid var(--white);
    background: linear-gradient(135deg, #b9c2c8 0%, #8d7a62 55%, #6a4a2e 100%);
  }
  .about-title { position: absolute; left: 533px; top: 30px; font-size: 19.5px; font-weight: 400; }
  .about-text { position: absolute; left: 532px; top: 78px; width: 506px; }
  .about-text p { font-size: 11.2px; line-height: 13.6px; margin-bottom: 13.5px; text-align: justify; }

  .products {
    position: absolute; top: 862px; left: 0; width: 1104px; height: 338px;
    background: radial-gradient(ellipse 600px 300px at 560px 120px, #2a3b44, var(--dark-deep));
  }
  .products-title { position: absolute; left: 0; width: 1104px; text-align: center; top: 30px; font-size: 39px; font-weight: 400; }
  .product-photo { position: absolute; border: 8px solid var(--white); }
  .product-panel { position: absolute; background: var(--brand-blue); text-align: center; }
  .product-name { position: absolute; left: 0; width: 100%; top: 80px; font-size: 27px; font-weight: 400; }
  .enquiry {
    position: absolute; top: 155px; width: 106px; height: 32px; border: 1px solid var(--white);
    font-size: 14.5px; line-height: 30px; color: var(--white); text-decoration: none; text-align: center;
  }
  .product-dark { position: absolute; background: var(--dark); }
</style>
</head>
<body>
  <header class="site-header">
    <div class="brand"><span class="brand-dot"></span><span class="brand-name">Netvale</span></div>
    <nav class="main-nav">
      <a href="#" style="left:520px">HOME</a>
      <a href="#" style="left:593px">ABOUT US</a>
      <a href="#" style="left:694px">PRODUCT</a>
      <a href="#" style="left:792px">TESTIMONIALS</a>
      <a href="#" style="left:925px">CONTACT US</a>
    </nav>
  </header>

  <section class="hero" role="img" aria-label="Underwater view of a school of fish swimming in blue-green water">
    <h1 class="hero-title">BEST SEA FOOD</h1>
    <p class="hero-sub">At Best Price</p>
  </section>
  <div class="scroll-cue">
    <svg width="24" height="16" viewBox="0 0 24 16"><polyline points="2,3 12,13 22,3" fill="none" stroke="#fff" stroke-width="2.5"/></svg>
  </div>

  <section class="about">
    <div class="about-photo" role="img" aria-label="Two fresh trout on a wooden board with lemon and basil"></div>
    <h2 class="about-title">ABOUT US</h2>
    <div class="about-text">
      <p>We are in the seafood business with a one man company sourcing and exporting frozen seafood We are in the seafood business with a one man company sourcing and exporting frozen seafood We are in the seafood business with a one man company sourcing and exporting frozen seafood We are in the seafood business with a one man company sourcing and exporting frozen seafood We are in the seafood business with a one man company sourcing and exporting frozen seafood</p>
      <p>We are in the seafood business with a one man company sourcing and exporting frozen seafood We are in the seafood business with a one man company sourcing and exporting frozen seafood We are in the seafood business with a one man company sourcing and exporting frozen seafood We are in the seafood business with a one man company sourcing and exporting frozen seafood We are in the seafood business with a one man company sourcing and exporting frozen seafood</p>
      <p>We are in the seafood business with a one man company sourcing and exporting frozen seafood We are in the seafood business with a one man company sourcing and exporting frozen seafood We are in the seafood business with a one man company sourcing and exporting frozen seafood We are in the seafood business with a one man company sourcing and exporting frozen seafood We are in the seafood business with a one man company sourcing and exporting frozen seafood</p>
    </div>
  </section>

  <section class="products">
    <h2 class="products-title">OUR PRODUCT</h2>

    <div class="product-photo" style="left:67px;top:96px;width:243px;height:223px;background:linear-gradient(160deg,#c9c4c8,#8e8f96 60%,#d4c9cc);" role="img" aria-label="Two hilsha fish on ice"></div>
    <div class="product-panel" style="left:310px;top:96px;width:243px;height:223px;">
      <h3 class="product-name">HILSHA</h3>
      <a class="enquiry" href="#" style="left:64px">ENQUIRY</a>
    </div>

    <div class="product-photo" style="left:553px;top:96px;width:247px;height:223px;background:linear-gradient(150deg,#3a3a3a,#7d8a99 45%,#e6e6e6);" role="img" aria-label="Fresh sea bass on a white wooden table"></div>
    <div class="product-panel" style="left:800px;top:96px;width:244px;height:223px;">
      <h3 class="product-name">HILSHA</h3>
      <a class="enquiry" href="#" style="left:59px">ENQUIRY</a>
    </div>

    <div class="product-dark" style="left:67px;top:319px;width:243px;height:30px;"></div>
    <div class="product-photo" style="left:310px;top:319px;width:243px;height:30px;border-bottom:none;background:linear-gradient(90deg,#c98b7e,#e0b3a6);" role="img" aria-label="Red fish fillets"></div>
    <div class="product-dark" style="left:553px;top:319px;width:247px;height:30px;"></div>
    <div class="product-photo" style="left:800px;top:319px;width:244px;height:30px;border-bottom:none;background:linear-gradient(90deg,#4a4038,#6b5d50);" role="img" aria-label="Seafood on a dark surface"></div>
  </section>
</body>
</html>
```